Business Card Design

Business Card for professional consulting firm working with large financial institutions.

Target Market(s)

Executive buyers

Industry/Entity Type

Banking

Contact Information for Business Card

Mild creativity wanted. Not boring, but do elaborate artwork.

Font styles to use
Serif
Sans Serif

Colors

Designer to choose colors to be used in the design.

Requirements
Must have
• Standard business card features - company name, individual name, telephone, website, email, locations.
Nice to have
• Two colors
Should not have
• too many colors, fancy printing, cartoons.

```html
<!DOCTYPE html>
<html lang="en">
<head>
<meta charset="utf-8">
<title>k7advisory business card</title>
<link rel="stylesheet" href="https://fonts.googleapis.com/css2?family=Old+Standard+TT:wght@400;700&display=swap">
<style>
  :root {
    --teal: #4a90a6;
    --silver: #c3c3c3;
    --paper: #ffffff;
    --mint: #b4eb98;
    --ink: #0c0c0c;
  }
  html, body {
    margin: 0;
    padding: 0;
    overflow: hidden;
  }
  .canvas {
    position: relative;
    width: 952px;
    height: 1200px;
    background: var(--mint);
    overflow: hidden;
    font-family: "Old Standard TT", Georgia, serif;
    color: var(--ink);
  }
  .card-front {
    position: absolute;
    left: 0;
    top: 0;
    width: 952px;
    height: 545px;
    background: var(--teal);
  }
  .card-front svg {
    position: absolute;
    left: 0;
    top: 0;
  }
  .brand-name {
    position: absolute;
    margin: 0;
    font-weight: 400;
    letter-spacing: -0.5px;
    white-space: nowrap;
    transform: translate(-50%, -50%);
    line-height: 1;
  }
  .brand-name--front {
    left: 227px;
    top: 244px;
    font-size: 58px;
  }
  .owner {
    position: absolute;
    margin: 0;
    left: 715px;
    top: 44px;
    transform: translateX(-50%);
    text-align: center;
    font-size: 40px;
    line-height: 48px;
    letter-spacing: 1px;
    white-space: nowrap;
  }
  .owner-name, .owner-title {
    display: block;
  }
  .contact-list {
    position: absolute;
    left: 0;
    top: 0;
    margin: 0;
    padding: 0;
    list-style: none;
  }
  .contact-item {
    position: absolute;
    left: 652px;
    transform: translateY(-50%);
    font-size: 24px;
    line-height: 1;
    letter-spacing: 0.5px;
    white-space: nowrap;
  }
  .contact-item--address { top: 231px; }
  .contact-item--phone { top: 313px; }
  .contact-item--email { top: 396px; }
  .contact-item--web { top: 488px; }
  .card-back {
    position: absolute;
    left: 0;
    top: 655px;
    width: 952px;
    height: 545px;
    background: var(--teal);
    border-left: 3px solid var(--mint);
    box-sizing: border-box;
  }
  .brand-name--back {
    left: 491px;
    top: 195px;
    font-size: 88px;
  }
  .rule {
    position: absolute;
    left: 0;
    width: 952px;
    background: var(--silver);
  }
  .rule--top { top: 322px; height: 5px; }
  .rule--mid { top: 336px; height: 15px; }
  .rule--low { top: 359px; height: 4px; }
</style>
</head>
<body>
<div class="canvas">
  <section class="card-front">
    <svg width="952" height="545" viewBox="0 0 952 545" aria-hidden="true">
      <path d="M523,0 C455,60 425,180 460,260 C500,360 575,440 580,545 L952,545 L952,0 Z" fill="var(--paper)"/>
      <path d="M523,0 C455,60 425,180 460,260 C500,360 575,440 580,545" fill="none" stroke="var(--silver)" stroke-width="14"/>
      <g class="contact-icons">
        <circle cx="610" cy="231" r="27" fill="var(--teal)"/>
        <path d="M610,250 C603,240 598,233 598,225 A12,12 0 0 1 622,225 C622,233 617,240 610,250 Z" fill="var(--ink)"/>
        <circle cx="610" cy="225" r="4.5" fill="var(--teal)"/>

        <circle cx="610" cy="313" r="27" fill="var(--teal)"/>
        <rect x="599" y="297" width="22" height="32" rx="5" fill="var(--ink)"/>
        <path d="M606,302 C603,310 604,318 609,324 L612,322 L610,316 L607,316 C606,312 606,309 607,306 L610,306 L611,300 Z" fill="var(--paper)"/>

        <circle cx="610" cy="396" r="27" fill="var(--teal)"/>
        <rect x="594" y="384" width="32" height="24" fill="var(--ink)"/>
        <path d="M594,384 L610,398 L626,384 M594,408 L605,394 M626,408 L615,394" stroke="var(--teal)" stroke-width="1.6" fill="none"/>

        <circle cx="610" cy="488" r="27" fill="var(--teal)"/>
        <g fill="none" stroke="var(--ink)" stroke-width="1.8">
          <circle cx="610" cy="488" r="16"/>
          <ellipse cx="610" cy="488" rx="7" ry="16"/>
          <line x1="610" y1="472" x2="610" y2="504"/>
          <line x1="594" y1="488" x2="626" y2="488"/>
          <path d="M597,479 H623 M597,497 H623"/>
        </g>
      </g>
    </svg>
    <p class="brand-name brand-name--front">k7advisory</p>
    <p class="owner">
      <span class="owner-name">owner’s name</span>
      <span class="owner-title">title</span>
    </p>
    <ul class="contact-list">
      <li class="contact-item contact-item--address">address</li>
      <li class="contact-item contact-item--phone">phone</li>
      <li class="contact-item contact-item--email">email</li>
      <li class="contact-item contact-item--web">website</li>
    </ul>
  </section>

  <section class="card-back">
    <p class="brand-name brand-name--back">k7advisory</p>
    <div class="rule rule--top"></div>
    <div class="rule rule--mid"></div>
    <div class="rule rule--low"></div>
  </section>
</div>
</body>
</html>
```